New corporate e-mail signature

We need a new e-mail signature for our company that is clean and professional. The requests are attached in a document.

Target Market(s)

CFO, CTO, Controllers, leaders, decision-makers.

Industry/Entity Type

Information Technology

Colors

Designer to choose colors to be used in the design.

Requirements
Must have
• See the PowerPoint document.
• - keep it as simple as possible.
• - same style as our new website design
• - It has to look good in all e-mail readers, and on all surfaces.
Nice to have
• - Please also attach 'best practise' for how to use the signature.
Should not have
• See the PowerPoint document. Use our color palette.
• - Do not include photo!

```html
<!DOCTYPE html>
<html lang="en">
<head>
<meta charset="utf-8">
<title>Quarrivel e-mail signature</title>
<link href="https://fonts.googleapis.com/css2?family=Montserrat:wght@400;500;600;700&display=swap" rel="stylesheet">
<style>
  :root {
    --page-bg: #f3f4fc;
    --card-bg: #ffffff;
    --teal: #22b3c0;
    --teal-light: #27bac3;
    --navy: #0d5585;
    --text-dark: #2b2b2b;
    --text-muted: #8a8a8a;
    --divider: #c9c9c9;
    --white: #ffffff;
  }
  * { box-sizing: border-box; margin: 0; padding: 0; }
  html, body {
    width: 1200px; height: 723px; overflow: hidden;
    background: var(--page-bg);
    font-family: "Montserrat", sans-serif;
  }
  .signature {
    position: absolute;
    top: 300px;
    width: 423px; height: 124px;
  }
  .signature--script { left: 100px; }
  .signature--caps { left: 684px; }
  .signature__card {
    position: absolute; left: 8px; top: 0; right: 0; bottom: 0;
    background: var(--card-bg);
    box-shadow: 0 4px 14px rgba(60, 60, 100, 0.12);
  }
  .signature__badge {
    position: absolute; left: 0; top: 1px;
    width: 122px; height: 122px; border-radius: 50%;
    background: linear-gradient(180deg, var(--teal-light) 0%, var(--navy) 100%);
    border: 2px solid var(--white);
    box-shadow: 0 2px 8px rgba(0, 0, 0, 0.12);
    display: flex; flex-direction: column; align-items: center; justify-content: center;
    gap: 7px;
  }
  .signature__brand {
    color: var(--white);
    font-weight: 700; font-size: 11px; letter-spacing: 0.3px;
    margin-top: 4px;
  }
  .signature__social { display: flex; gap: 9px; }
  .signature__social span {
    width: 6px; height: 6px; border-radius: 50%; background: var(--white);
  }
  .signature__website {
    position: absolute; left: 140px; top: 56px;
    font-size: 6.5px; font-weight: 500; color: var(--text-dark); letter-spacing: 0.2px;
  }
  .signature__divider {
    position: absolute; left: 227px; top: 48px;
    width: 1px; height: 24px; background: var(--divider);
  }
  .signature__details { position: absolute; left: 252px; top: 26px; }
  .signature__name {
    font-size: 13.5px; font-weight: 600; color: var(--teal); letter-spacing: 0.2px;
  }
  .signature__role {
    font-size: 8px; color: var(--text-muted); letter-spacing: 0.3px; margin-top: 2px;
  }
  .signature__contact {
    display: flex; align-items: center; gap: 9px;
    font-size: 8.5px; color: var(--text-dark); margin-top: 9px;
  }
  .signature__contact + .signature__contact { margin-top: 10px; }
  .signature__contact svg { width: 9px; height: 9px; flex: none; }
  .icon-fill { fill: var(--teal); }
  .icon-line { fill: none; stroke: var(--white); stroke-width: 0.9; }
</style>
</head>
<body>

<section class="signature signature--script">
  <div class="signature__card"></div>
  <div class="signature__badge">
    <span class="signature__brand">Quarrivel</span>
    <div class="signature__social" role="img" aria-label="Social media links"><span></span><span></span><span></span></div>
  </div>
  <p class="signature__website">www.quarrivel.example</p>
  <div class="signature__divider"></div>
  <div class="signature__details">
    <p class="signature__name">Martin Lewell</p>
    <p class="signature__role">General Manager</p>
    <p class="signature__contact">
      <svg viewBox="0 0 10 10" aria-hidden="true"><rect class="icon-fill" x="0" y="2" width="10" height="6.5"/><polyline class="icon-line" points="0.4,2.4 5,5.8 9.6,2.4"/></svg>
      martin@quarrivel.example
    </p>
    <p class="signature__contact">
      <svg viewBox="0 0 10 10" aria-hidden="true"><path class="icon-fill" d="M2.2 0.6 L3.8 2.8 L2.9 4 Q4 6.2 6 7.1 L7.2 6.2 L9.4 7.8 L8.4 9.4 Q4.8 9.4 2.4 6.8 Q0.4 4.4 0.6 1.6 Z"/></svg>
      001 555 014 2290
    </p>
  </div>
</section>

<section class="signature signature--caps">
  <div class="signature__card"></div>
  <div class="signature__badge">
    <span class="signature__brand">QUARRIVEL</span>
    <div class="signature__social" role="img" aria-label="Social media links"><span></span><span></span><span></span></div>
  </div>
  <p class="signature__website">www.quarrivel.example</p>
  <div class="signature__divider"></div>
  <div class="signature__details">
    <p class="signature__name">Martin Lewell</p>
    <p class="signature__role">General Manager</p>
    <p class="signature__contact">
      <svg viewBox="0 0 10 10" aria-hidden="true"><rect class="icon-fill" x="0" y="2" width="10" height="6.5"/><polyline class="icon-line" points="0.4,2.4 5,5.8 9.6,2.4"/></svg>
      martin@quarrivel.example
    </p>
    <p class="signature__contact">
      <svg viewBox="0 0 10 10" aria-hidden="true"><path class="icon-fill" d="M2.2 0.6 L3.8 2.8 L2.9 4 Q4 6.2 6 7.1 L7.2 6.2 L9.4 7.8 L8.4 9.4 Q4.8 9.4 2.4 6.8 Q0.4 4.4 0.6 1.6 Z"/></svg>
      001 555 014 2290
    </p>
  </div>
</section>

</body>
</html>
```